Private School Website Revamp

We need a new design for the private school's website revamp. The new website will be using WordPress CMS, but we will be using it to handle custom data types, not blogs - so the content will not be typical blog-style.

The school has indicated the following template which they like, and our design to follow the design style.
http://mvr7.layout-demoes.com/sitetheme_48172/
However, follow the school's colour-theme and sitemap.

Colour-theme: White, Green (refer to current website - www.ruolinvo.com.sg)

Sitemap: (for navigation menu)
- Home
- Academic & Examination Board
- Our Philosophy
- Our Programmes
+ Preparatory Courses
+ Tuition Classes
+ Study Tours
- Our Hostel
- Trial Tests
+ English
+ Mathematics
- Contact Us

Target Market(s)

Parents looking for private school services.
Existing students of the private school accessing trial tests.

Industry/Entity Type

School

Requirements
Must have
• Homepage design to include
• - Logo, navigation menu, search box
• - Featured area/slideshow (see prefered template above)
• - Section for Preparatory Courses
• - Section for Tuition Classes
• - Section for Study Tours
• - Section for Hostel Stay
• - Awards & Certification box
• - Footer contact details
Nice to have
• - Pictures of happy students
• - The Message from Director box is "nice to have", but no necessary if it does not fit into homepage design.

```html
<!DOCTYPE html>
<html lang="en">
<head>
<meta charset="utf-8">
<title>Ruolin Private School</title>
<link href="https://fonts.googleapis.com/css2?family=Cabin:wght@400;600&family=Carlito&family=Open+Sans:ital,wght@0,400;1,600;1,700&display=swap" rel="stylesheet">
<style>
:root{
  --sky:#b9d9ec;
  --sky-light:#e6f1f8;
  --brand-green:#0f4a18;
  --text:#2a2a2a;
  --nav-text:#2b3a44;
  --pill:#1a9be0;
  --link-red:#b0141a;
  --frame-grey:#8a8a8a;
  --awards-bg:#d8d8dc;
  --card-cyan-a:#3fd7f5;--card-cyan-b:#36b9f0;
  --card-orange-a:#f29a2b;--card-orange-b:#f7c636;
  --card-green-a:#68c52a;--card-green-b:#b9e33a;
  --card-blue-a:#1b9fd8;--card-blue-b:#4fb3d6;
}
*{box-sizing:border-box;margin:0;padding:0}
html,body{width:1055px;height:1200px;overflow:hidden}
body{position:relative;font-family:"Cabin",sans-serif;color:var(--text);
  background:linear-gradient(180deg,var(--sky) 0,var(--sky-light) 420px,#fff 760px,#fff 100%)}
.abs{position:absolute}
.logo{left:46px;top:19px;display:flex;align-items:center;gap:8px}
.logo-mark{width:18px;height:18px;background:var(--brand-green);border-radius:3px}
.logo-name{font-family:"Cabin",sans-serif;font-weight:600;font-size:19px;color:var(--brand-green);letter-spacing:.5px}
.search{left:796px;top:54px;display:flex;gap:10px}
.search-input{width:128px;height:24px;border:1px solid #333;background:#fff}
.search-btn{width:53px;height:24px;border-radius:6px;background:var(--pill);color:#fff;font-size:12.5px;border:1px solid #0b7cb8;display:flex;align-items:center;justify-content:center}
.nav{left:205px;top:112px;display:flex;align-items:center;font-size:13.5px;color:var(--nav-text)}
.nav span.sep{margin:0 9px}
.nav .current{background:var(--pill);color:#fff;padding:3px 8px;border-radius:4px;height:24px;display:flex;align-items:center}
.hero{left:46px;top:145px;width:964px;height:292px;border:2px solid #fff;border-radius:6px;
  background:linear-gradient(135deg,#6f7a58 0%,#b39a7c 35%,#8c6e52 60%,#c9b08a 100%)}
.welcome{left:46px;top:455px;width:472px;height:606px;border:4px solid var(--frame-grey);border-radius:12px;
  background:linear-gradient(180deg,#fff 0,#f1f6fa 100%);padding:0 20px}
.welcome h1{font-family:"Carlito",sans-serif;font-weight:400;font-size:31px;color:#333;margin:24px 0 8px 8px}
.welcome p{font-size:12.8px;line-height:21px;text-align:justify;letter-spacing:.2px}
.welcome p+p{margin-top:21px}
.welcome .tight{margin-top:0!important}
.sign{display:flex;gap:20px;margin-top:8px}
.portrait{width:60px;height:76px;background:linear-gradient(180deg,#5d6c7c,#2c2f36);border:2px solid #333;margin-left:2px}
.sign-text{font-size:12.8px;line-height:21px;padding-top:16px}
.card{width:227px;height:62px;border-radius:7px;display:flex;align-items:center;gap:10px;padding-left:10px;
  color:#fff;font-family:"Open Sans",sans-serif;font-style:italic;font-weight:600;font-size:16px;text-shadow:0 1px 2px rgba(0,0,0,.45)}
.card.prep{left:548px;top:456px;background:linear-gradient(180deg,var(--card-cyan-a),var(--card-cyan-b))}
.card.tuition{left:786px;top:456px;background:linear-gradient(180deg,var(--card-orange-a),var(--card-orange-b))}
.card.tours{left:559px;top:634px;background:linear-gradient(90deg,var(--card-green-a),var(--card-green-b))}
.card.hostel{left:795px;top:634px;background:linear-gradient(90deg,var(--card-blue-a),var(--card-blue-b))}
.blurb{width:205px;font-size:12.8px;line-height:21px;letter-spacing:.3px}
.more{font-size:11.5px;color:var(--link-red);text-align:right;margin-top:6px}
.divider{width:0;border-left:2px dotted #999}
.awards{left:572px;top:828px;width:446px;height:233px;border-radius:12px;
  background:linear-gradient(180deg,#cfcfd3,#e6e6ea)}
.awards h2{position:absolute;left:29px;top:14px;font-family:"Open Sans",sans-serif;font-style:italic;font-weight:700;
  font-size:25px;color:#555;text-shadow:1px 1px 2px #fff;letter-spacing:.5px}
.trophy{position:absolute;left:0;top:62px;width:140px;height:171px;border-radius:0 0 0 12px;
  background:linear-gradient(180deg,#c4c4c8,#d4d4d8)}
.badge-a{position:absolute;left:148px;top:62px;width:162px;height:74px;background:#0a49a0}
.badge-b{position:absolute;left:152px;top:148px;width:104px;height:74px;background:#627a56}
.awards .cap{position:absolute;font-size:13px;line-height:21px;color:#333}
.footer-rule{left:0;top:1083px;width:1055px;height:2px;background:#888}
.contact{left:65px;top:1097px;font-size:9.5px;line-height:16px;color:#333}
.copy{right:65px;top:1097px;font-size:9.5px;color:#333}
</style>
</head>
<body>
<header>
  <div class="abs logo"><span class="logo-mark"></span><span class="logo-name">RUOLIN PRIVATE SCHOOL</span></div>
  <div class="abs search"><div class="search-input"></div><div class="search-btn">Search</div></div>
  <nav class="abs nav">
    <span class="current">Home</span><span class="sep">|</span>
    <span>Academic &amp; Examination Board</span><span class="sep">|</span>
    <span>Our Philosophy</span><span class="sep">|</span>
    <span>Our Programmes</span><span class="sep">|</span>
    <span>Our Hostel</span><span class="sep">|</span>
    <span>Trial Tests</span><span class="sep">|</span>
    <span>Contact Us</span>
  </nav>
</header>

<div class="abs hero" role="img" aria-label="Photo of four smiling students with backpacks"></div>

<section class="abs welcome">
  <h1>Welcome to Ruolin Private School</h1>
  <p>Ruolin Private School was founded to meet the growing demand of foreign students seeking an effective bilingual education in Singapore.</p>
  <p>We are managed by a group of professionals who are formerly Ministry of Education senior officers and we have a team of dedicated, qualified and experienced part time teachers who are committed to help you succeed.</p>
  <p>In order for our students to focus their full attention on their studies, we provide a conducive learning environment through a low teacher-student ratio of 1:15 and properly equipped classrooms. There are 5 such classrooms in the school, able to hold between 11 to 15 students per class, based on the guidelines prescribed by the Ministry of Education.</p>
  <p class="tight">With this, we wish you every success in your learning journey with us and we believe you will find your journey here an excellent chance for personal growth and development.</p>
  <p>Yours sincerely,</p>
  <div class="sign">
    <div class="portrait" role="img" aria-label="Portrait photo of the director"></div>
    <div class="sign-text">Mr Lim Wei Jun<br>Director<br>Ruolin Private School</div>
  </div>
</section>

<div class="abs card prep">
  <svg width="38" height="44" viewBox="0 0 38 44"><rect x="4" y="4" width="26" height="36" rx="2" fill="#fff"/><rect x="26" y="2" width="8" height="40" fill="#333"/><rect x="9" y="12" width="12" height="2" fill="#999"/><rect x="9" y="18" width="12" height="2" fill="#999"/><rect x="14" y="24" width="6" height="10" fill="#c33"/></svg>
  PREPATORY COURSES
</div>
<div class="abs card tuition">
  <svg width="44" height="36" viewBox="0 0 44 36"><rect x="8" y="2" width="34" height="24" fill="#2a7a2a" stroke="#6b4a2a" stroke-width="2"/><line x1="14" y1="20" x2="28" y2="8" stroke="#e8e860" stroke-width="2"/><circle cx="8" cy="28" r="6" fill="#c22"/></svg>
  TUTION CLASSES
</div>
<div class="abs card tours">
  <svg width="38" height="38" viewBox="0 0 38 38"><rect width="38" height="38" rx="8" fill="#f06a1e"/><rect x="6" y="11" width="26" height="14" rx="3" fill="#fff"/><rect x="9" y="14" width="20" height="5" fill="#f06a1e"/><circle cx="12" cy="27" r="2.5" fill="#fff"/><circle cx="26" cy="27" r="2.5" fill="#fff"/></svg>
  STUDY TOURS
</div>
<div class="abs card hostel">
  <svg width="38" height="38" viewBox="0 0 38 38"><rect width="38" height="38" rx="8" fill="#5cc23a"/><rect x="12" y="7" width="14" height="26" fill="#fff"/><rect x="15" y="11" width="3" height="3" fill="#5cc23a"/><rect x="20" y="11" width="3" height="3" fill="#5cc23a"/><rect x="15" y="17" width="3" height="3" fill="#5cc23a"/><rect x="20" y="17" width="3" height="3" fill="#5cc23a"/><rect x="15" y="23" width="3" height="3" fill="#5cc23a"/><rect x="20" y="23" width="3" height="3" fill="#5cc23a"/></svg>
  HOSTEL STAY
</div>

<div class="abs blurb" style="left:571px;top:528px">Nulla dui. Fusce feuaada ore. Mauris fermentum dictum gna. Sedaoreet aliquam leo. Ut<div class="more" style="margin-right:-1px">Read more</div></div>
<div class="abs divider" style="left:785px;top:530px;height:86px"></div>
<div class="abs blurb" style="left:808px;top:523px">Nulla dui. Fusce feuaada ore. Mauris fermentum dictum gna. Sedaoreet aliquam leo. Ut<div class="more" style="margin-right:-10px">Read more</div></div>
<div class="abs blurb" style="left:580px;top:714px">Nulla dui. Fusce feuaada ore. Mauris fermentum dictum gna. Sedaoreet aliquam leo. Ut<div class="more" style="margin-top:0;margin-right:-2px">Read more</div></div>
<div class="abs divider" style="left:792px;top:705px;height:86px"></div>
<div class="abs blurb" style="left:822px;top:714px">Nulla dui. Fusce feuaada ore. Mauris fermentum dictum gna. Sedaoreet aliquam leo. Ut<div class="more" style="margin-top:4px;margin-right:-8px">Read more</div></div>

<section class="abs awards">
  <h2>AWARDS &amp; CERTIFICATIONS</h2>
  <div class="trophy" role="img" aria-label="Faint trophy decoration"></div>
  <div class="badge-a" role="img" aria-label="Accreditation badge"></div>
  <div class="cap" style="left:316px;top:79px">Ruolin Private<br>School</div>
  <div class="badge-b" role="img" aria-label="Education award badge"></div>
  <div class="cap" style="left:270px;top:197px">Ruolin Student Hostel</div>
</section>

<div class="abs footer-rule"></div>
<footer>
  <address class="abs contact" style="font-style:normal">14 Bukit Orchid Ave 31<br>Kembang Community Hall, #02-07<br>S(604518)<br>Tel: +65 6381 4472<br>Fax: +65 6381 4473<br>Email: school@ruolinvo.com.sg</address>
  <div class="abs copy">© 2010. Ruolin Private School.</div>
</footer>
</body>
</html>
```